Website 950x200 Header w/ logo

I'm in need of a website header for a new site called TalesofGordo.com

The site is basically a glorified blog for myself to write my thoughts about politics, sports, TV shows, current events, whatever. I have a lot of interests.

The site is going to look very very similar to http://www.quillpostmedia.com/5930417/7-tips-for-hiring-bold-minds

but instead of having a dynamic header that becomes the picture with each article, its just going to be a static header in which I'd like to have the name of the site (Tales of Gordo) and some kind of logo, pictures, etc - I'm totally open to anything. The only thing is it needs to have a dark (probably black) background and needs to be 950x200px.

I envision a black background, with gray and white as the primary colors and then some secondary colors potentially, but again I'm open to anything as long as it's on the black background or some kind of charcoal gray or wahtever. On the site the black part will go all the way from the left of the screen to the right no matter what the window size, but I'd like to keep all the content inside of 950x200px

email me gordo.pellwick@zentramail.com if you have any questions. Thanks!

```html
<!DOCTYPE html>
<html lang="en">
<head>
<meta charset="utf-8">
<title>Tales of Gordo Header</title>
<link rel="stylesheet" href="https://fonts.googleapis.com/css2?family=Ubuntu:ital,wght@0,400;1,400&display=swap">
<style>
  :root {
    --top-light: #5d6266;
    --top-dark: #43474a;
    --nav-light: #46546c;
    --nav-dark: #2b3850;
    --nav-active: #6c7681;
    --divider: #d7dbe0;
    --logo-text: #e2e2de;
    --share-text: #2b2e31;
    --share-line: #d9dcde;
    --icon-one: #2f4680;
    --icon-two: #7fbfd3;
    --icon-three: #2f8f96;
    --icon-four: #e48a1c;
    --btn-light: #d3d3d0;
    --btn-dark: #a9a9a6;
    --btn-text: #6a6a6a;
    --field-bg: #dcdcd4;
    --field-text: #a3a39e;
    --white: #ffffff;
  }
  * { margin: 0; padding: 0; box-sizing: border-box; }
  html, body { width: 1200px; height: 253px; overflow: hidden; background: var(--top-dark); }
  .header { position: relative; width: 1200px; height: 253px; font-family: "Ubuntu", sans-serif; }
  .topbar {
    position: absolute; left: 0; top: 0; width: 1200px; height: 163px;
    background: linear-gradient(to bottom, var(--top-light), var(--top-dark));
  }
  .brand-name {
    position: absolute; left: 18px; top: 58px; height: 52px;
    font-weight: 400; font-size: 44px; line-height: 52px;
    color: var(--logo-text); white-space: nowrap;
  }
  .share { position: absolute; left: 543px; top: 51px; display: flex; align-items: center; height: 62px; }
  .share-label { font-size: 35px; color: var(--share-text); margin-right: 10px; }
  .share-icon { width: 58px; height: 58px; border-radius: 50%; }
  .share-icon.one { background: var(--icon-one); }
  .share-icon.two { background: var(--icon-two); }
  .share-icon.three { background: var(--icon-three); }
  .share-icon.four { background: var(--icon-four); }
  .share-sep { width: 3px; height: 50px; background: var(--share-line); margin: 0 10px; border-radius: 1px; }
  .subscribe {
    position: absolute; left: 962px; top: 56px; width: 213px; height: 54px;
    border-radius: 10px; background: linear-gradient(to bottom, var(--btn-light), var(--btn-dark));
    color: var(--btn-text); font-size: 32px; text-align: center; line-height: 54px;
    box-shadow: 0 1px 2px rgba(0,0,0,0.4);
  }
  .nav {
    position: absolute; left: 0; top: 163px; width: 1200px; height: 90px;
    background: linear-gradient(to bottom, var(--nav-light), var(--nav-dark));
    border-top: 1px solid #6a7588;
  }
  .nav-item {
    position: absolute; top: 0; height: 90px; line-height: 90px;
    font-size: 35px; color: var(--white); padding-left: 23px;
  }
  .nav-item.active { left: 0; width: 143px; background: linear-gradient(to bottom, #7a838d, var(--nav-active)); }
  .nav-divider { position: absolute; top: 0; width: 4px; height: 90px; background: var(--divider); box-shadow: 1px 0 2px rgba(0,0,0,0.5); }
  .search {
    position: absolute; left: 842px; top: 184px; width: 333px; height: 56px;
    border-radius: 28px; background: var(--field-bg);
    box-shadow: inset 0 2px 3px rgba(0,0,0,0.35);
  }
  .search-text { position: absolute; left: 27px; top: 0; line-height: 56px; font-size: 32px; font-style: italic; color: var(--field-text); }
  .search-icon { position: absolute; right: 22px; top: 14px; }
</style>
</head>
<body>
<header class="header">
  <div class="topbar">
    <span class="brand-name">Tales of Gordo</span>
    <div class="share">
      <span class="share-label">share</span>
      <span class="share-icon one"></span>
      <span class="share-sep"></span>
      <span class="share-icon two"></span>
      <span class="share-sep"></span>
      <span class="share-icon three"></span>
      <span class="share-sep"></span>
      <span class="share-icon four"></span>
    </div>
    <div class="subscribe">Subscribe</div>
  </div>
  <nav class="nav">
    <span class="nav-item active">Home</span>
    <span class="nav-divider" style="left:143px"></span>
    <span class="nav-item" style="left:151px">Politics</span>
    <span class="nav-divider" style="left:323px"></span>
    <span class="nav-item" style="left:327px">Sports</span>
    <span class="nav-divider" style="left:477px"></span>
    <span class="nav-item" style="left:478px">TV Shows</span>
    <span class="nav-divider" style="left:680px"></span>
  </nav>
  <div class="search">
    <span class="search-text">search</span>
    <svg class="search-icon" width="30" height="30" viewBox="0 0 30 30">
      <circle cx="18" cy="12" r="8" fill="none" stroke="#a3a39e" stroke-width="3"/>
      <line x1="12" y1="18" x2="3" y2="27" stroke="#a3a39e" stroke-width="4" stroke-linecap="round"/>
    </svg>
  </div>
</header>
</body>
</html>
```